Re-Design of Business Card for Marine Sales People

We are looking to Re-design our business cards to look like they are in the 21st century. We are a full service marina and sell a lot of new/used boats. May want a spot on the card for our 3 main brands we sell. A picture spot of the sales man would be nice, but not necessarily.

```html
<!DOCTYPE html>
<html lang="en">
<head>
<meta charset="UTF-8">
<title>Lakeshore Harbor – Business Card</title>
<link href="https://fonts.googleapis.com/css2?family=Montserrat:wght@400;500;700;800&family=Libre+Baskerville:wght@700&display=swap" rel="stylesheet">
<style>
  :root {
    --backdrop: #d4d6d9;
    --navy: #142c55;
    --navy-light: #5f7594;
    --sky: #2b8bc9;
    --ink: #1d3558;
    --paper: #f1f1f1;
    --white: #ffffff;
  }
  * { box-sizing: border-box; margin: 0; padding: 0; }
  html, body { width: 1200px; height: 1200px; overflow: hidden; }
  body {
    background: var(--backdrop);
    font-family: "Montserrat", Arial, sans-serif;
    position: relative;
  }
  .card {
    position: absolute;
    left: 220px;
    width: 760px;
    height: 434px;
    border-radius: 26px;
    box-shadow: 0 10px 28px rgba(0,0,0,0.22);
    overflow: hidden;
  }
  /* Front */
  .card-front {
    top: 100px;
    background: linear-gradient(100deg, var(--navy-light) 0%, #3f5578 35%, var(--navy) 70%);
    color: var(--white);
    display: flex;
    flex-direction: column;
    align-items: center;
    justify-content: center;
  }
  .brand-name {
    font-family: "Montserrat", Arial, sans-serif;
    font-weight: 700;
    letter-spacing: 4px;
    text-transform: uppercase;
    display: flex;
    align-items: center;
    gap: 14px;
    white-space: nowrap;
  }
  .brand-dot {
    width: 16px; height: 16px; border-radius: 50%;
    background: currentColor;
    flex: none;
  }
  .card-front .brand-name { font-size: 44px; color: var(--white); }
  .tagline {
    margin-top: 70px;
    font-family: "Libre Baskerville", Georgia, serif;
    font-weight: 700;
    font-size: 22px;
    text-align: center;
    line-height: 1.5;
  }
  .tagline-rule {
    display: block;
    width: 150px; height: 2px;
    margin: 2px auto 4px;
    background: var(--sky);
  }
  /* Back */
  .card-back {
    top: 630px;
    background: var(--paper);
    color: var(--ink);
    padding: 36px 48px 38px;
    display: flex;
    flex-direction: column;
    justify-content: space-between;
  }
  .card-back .brand-name {
    font-size: 34px; color: var(--ink);
    justify-content: center;
  }
  .person { text-align: center; }
  .person-name { color: var(--sky); font-weight: 800; font-size: 34px; line-height: 1.1; }
  .person-title { font-size: 18px; font-weight: 500; color: var(--ink); }
  .locations {
    display: flex;
    justify-content: center;
  }
  .location { width: 280px; font-size: 17px; line-height: 1.4; }
  .location-left { text-align: right; padding-right: 24px; }
  .location-right { text-align: left; padding-left: 24px; }
  .divider { width: 2px; background: var(--ink); }
  .location-name {
    font-weight: 700; font-size: 18px;
    padding-bottom: 3px;
    border-bottom: 2px solid var(--sky);
    margin-bottom: 5px;
  }
  .phone {
    display: inline-flex; align-items: center; gap: 8px;
    margin-top: 6px; font-size: 18px;
  }
  .contact-row {
    display: flex;
    justify-content: space-between;
    font-size: 18px;
  }
  .contact { display: flex; align-items: center; gap: 10px; }
  .icon { width: 18px; height: 18px; flex: none; fill: var(--sky); }
</style>
</head>
<body>

<section class="card card-front">
  <div class="brand-name"><span class="brand-dot"></span>Lakeshore Harbor</div>
  <p class="tagline">“Setting Sail”<span class="tagline-rule"></span>Since 1984</p>
</section>

<section class="card card-back">
  <div class="brand-name"><span class="brand-dot"></span>Lakeshore Harbor</div>

  <div class="person">
    <div class="person-name">Dana</div>
    <div class="person-title">Director</div>
  </div>

  <div class="locations">
    <div class="location location-left">
      <div class="location-name">Harborview</div>
      <div>42 Dockside Rd. Millbrook,<br>NH 03999</div>
      <div class="phone">(555) 210-4417
        <svg class="icon" viewBox="0 0 24 24" aria-hidden="true"><path d="M6.6 10.8a15 15 0 0 0 6.6 6.6l2.2-2.2a1 1 0 0 1 1-.25 11.4 11.4 0 0 0 3.6.57 1 1 0 0 1 1 1V20a1 1 0 0 1-1 1A17 17 0 0 1 3 4a1 1 0 0 1 1-1h3.5a1 1 0 0 1 1 1c0 1.25.2 2.45.57 3.57a1 1 0 0 1-.25 1z"/></svg>
      </div>
    </div>
    <div class="divider"></div>
    <div class="location location-right">
      <div class="location-name">Harborview</div>
      <div>42 Dockside Rd. Millbrook,<br>NH 03999</div>
      <div class="phone">
        <svg class="icon" viewBox="0 0 24 24" aria-hidden="true"><path d="M6.6 10.8a15 15 0 0 0 6.6 6.6l2.2-2.2a1 1 0 0 1 1-.25 11.4 11.4 0 0 0 3.6.57 1 1 0 0 1 1 1V20a1 1 0 0 1-1 1A17 17 0 0 1 3 4a1 1 0 0 1 1-1h3.5a1 1 0 0 1 1 1c0 1.25.2 2.45.57 3.57a1 1 0 0 1-.25 1z"/></svg>
        (555) 318-2290</div>
    </div>
  </div>

  <div class="contact-row">
    <div class="contact">
      <svg class="icon" viewBox="0 0 24 24" aria-hidden="true"><path d="M2 5h20v14H2z" opacity=".9"/><path d="M2 5l10 8 10-8" fill="none" stroke="#f1f1f1" stroke-width="1.8"/></svg>
      dana@lakeshoreharbor.com
    </div>
    <div class="contact">
      <svg class="icon" viewBox="0 0 24 24" aria-hidden="true"><circle cx="12" cy="12" r="10"/><path d="M2 12h20M12 2c3 3 3 17 0 20M12 2c-3 3-3 17 0 20" fill="none" stroke="#f1f1f1" stroke-width="1.5"/></svg>
      www.lakeshoreharbor.com
    </div>
  </div>
</section>

</body>
</html>
```